WordPress Website Design - Tolvey Auction

Need a WordPress design for an auction company wanting a responsive, simple and easy to use site.
Sites the client mentions liking - www.brindlegavel.example, http://www.quellor.example and http://www.pardwick.example/. The logo is attached. Site color can be changed to suit your design. Also consider the attached graphic for email lists.

Industry/Entity Type

It Company

Number of Pages Required

1 page

Font styles to use
Serif
Sans Serif

Requirements
Must have
• Will be graphic intensive with full width slideshow. tagline to be used – “Let Our Experience Work for You! The background of the site can be the background of the attached image. The feel of the site can be the attached email template.
• Navigation: 1)Home 2) Tolvey Services 3) Featured Projects 4) Results 5) Buying/Selling 6) About Tolvey 7) Contact us
• Colors will be those on current site and those in the email template.
• Calls to action on the homepage:1) Marketing Consultation, 2) Marketing Plan Implementation, 3) Coordination of Related Marketing Services, 4)Featured Projects, 5) Negotiated Sales
• widgets can include upcoming auctions, email signup, news & events
• Choice of the company logo to use- light or dark.
• Footer will have contact info, a testimonial widget,and associated logos (attached)
• contact info:
• Tolvey Companies, Inc
• P.O. Box 4382
• Larkmoor, ND 58204
• tolvey@tolveycompanies.example
• (701) 555-0187 • Fax (701) 555-0143
Nice to have
• Use of drop down menus - under "Results"
• 1) Auction Results
• 2) Sales results

```html
<!DOCTYPE html>
<html lang="en">
<head>
<meta charset="utf-8">
<title>Tolvey Auction</title>
<link href="https://fonts.googleapis.com/css2?family=Open+Sans:ital,wght@0,400;0,600;0,700;1,400&family=Lora:ital,wght@1,400&display=swap" rel="stylesheet">
<style>
:root{
  --red:#c9202b;
  --red-dark:#a5161f;
  --ink:#333;
  --muted:#777;
  --light:#f3f3f3;
  --band:#e4e4e4;
  --footer:#2b2b2b;
  --footer-deep:#1e1e1e;
  --white:#fff;
}
*{box-sizing:border-box;margin:0;padding:0}
html,body{width:1200px;height:2492px;overflow:hidden}
body{font-family:"Open Sans",Arial,sans-serif;color:var(--ink);background:var(--light);font-size:12px;position:relative}

/* header */
.site-header{position:absolute;top:0;left:0;width:1200px;height:152px;background:var(--white)}
.brand{position:absolute;left:80px;top:30px;display:flex;align-items:center;gap:12px}
.brand-dot{width:56px;height:56px;border-radius:50%;background:var(--red)}
.brand-name{font-size:24px;font-weight:700;color:var(--ink)}
.topbar{position:absolute;right:110px;top:14px;display:flex;align-items:center;gap:18px;font-size:11px;color:var(--muted)}
.topbar span{display:flex;align-items:center;gap:6px}
.social-dots{display:flex;gap:6px}
.social-dots i{width:16px;height:16px;border-radius:50%;background:#bbb;display:block}
.main-nav{position:absolute;right:110px;top:100px;display:flex;gap:26px;font-size:11px;font-weight:600;text-transform:uppercase;color:#555}
.main-nav a{color:inherit;text-decoration:none;padding-bottom:8px}
.main-nav a.active{color:var(--red);border-bottom:2px solid var(--red)}

/* hero */
.hero{position:absolute;top:152px;left:0;width:1200px;height:520px;background:linear-gradient(120deg,#5a6670 0%,#8a959c 40%,#6f7a80 70%,#4b555c 100%)}
.hero-title{position:absolute;left:130px;top:205px;color:var(--white);font-size:44px;font-weight:700;line-height:1.15;text-shadow:0 2px 6px rgba(0,0,0,.4)}
.btn-hero{position:absolute;left:130px;top:318px;background:var(--red);color:var(--white);font-weight:700;font-size:16px;padding:12px 22px;letter-spacing:.5px}
.hero-arrow{position:absolute;top:240px;width:34px;height:34px;background:rgba(0,0,0,.35);display:flex;align-items:center;justify-content:center}

/* services */
.services{position:absolute;top:672px;left:0;width:1200px;height:400px}
.tool-badge{position:absolute;left:580px;top:12px;width:40px;height:40px;border-radius:50%;background:var(--white);display:flex;align-items:center;justify-content:center;box-shadow:0 1px 3px rgba(0,0,0,.2)}
.section-title{position:absolute;left:0;width:1200px;text-align:center;font-size:34px;font-weight:400;color:var(--ink)}
.section-title em{font-style:normal;color:var(--red);font-weight:600}
.services .section-title{top:52px}
.title-rule{position:absolute;left:570px;width:60px;height:2px;background:var(--red)}
.service{position:absolute;top:128px;width:190px;text-align:center}
.service-icon{width:88px;height:88px;border-radius:50%;background:var(--red);margin:0 auto;display:flex;align-items:center;justify-content:center;border:4px solid #e7b5b8}
.service h3{font-size:13px;font-weight:600;margin-top:14px;line-height:1.3;min-height:34px}
.service p{font-size:10px;color:var(--muted);margin-top:8px;line-height:1.5}
.btn-small{display:inline-block;background:var(--red);color:var(--white);font-size:9px;padding:3px 10px;margin-top:10px}
.svc-arrow{position:absolute;top:160px;color:#888;font-size:26px}

/* welcome */
.welcome{position:absolute;top:1072px;left:0;width:1200px;height:248px;background:var(--band)}
.welcome .section-title{top:48px;font-size:36px}
.welcome p{position:absolute;left:200px;top:110px;width:800px;text-align:center;font-size:11px;color:var(--muted);line-height:1.7}
.welcome .btn-small{position:absolute;left:552px;top:184px;font-size:12px;padding:6px 14px}

/* widgets */
.panel{position:absolute;background:var(--white)}
.panel-head{background:var(--red);color:var(--white);font-size:12px;font-weight:700;text-transform:uppercase;padding:6px 12px;display:flex;justify-content:space-between}
.thumbs{display:flex;gap:16px;padding:14px 12px}
.thumb{width:148px}
.thumb .img{height:110px;background:linear-gradient(180deg,#a9c4dc 0%,#c9c2b2 55%,#7d9a5c 100%)}
.thumb h4{font-size:10px;font-weight:700;margin-top:8px}
.thumb p{font-size:9px;color:var(--muted);margin-top:4px;line-height:1.4}
.thumb .btn-small{background:#555;margin-top:6px}
.video{height:180px;margin:10px;background:linear-gradient(160deg,#9bb0c2 0%,#b9a98f 60%,#6b7a54 100%);position:relative}
.play{position:absolute;left:108px;top:60px;width:50px;height:50px;border-radius:50%;background:rgba(0,0,0,.45);display:flex;align-items:center;justify-content:center}
.motd{background:var(--red);color:var(--white);padding:14px 14px}
.motd h3{font-family:"Lora",Georgia,serif;font-style:italic;font-weight:400;font-size:22px}
.motd p{font-size:10px;margin-top:6px;line-height:1.5}
.news-item{display:flex;gap:10px;padding:12px;border-bottom:1px solid #eee}
.date{width:38px;height:42px;background:#eee;text-align:center;flex:none}
.date b{display:block;font-size:16px;color:var(--red);padding-top:3px}
.date small{font-size:8px;color:var(--muted)}
.news-item h4{font-size:10px;font-weight:700}
.news-item p{font-size:9px;color:var(--muted);margin-top:3px;line-height:1.4}
.testi-head{display:flex;align-items:center;gap:10px;font-size:13px;font-weight:700;text-transform:uppercase;color:var(--ink);padding:12px}
.testi-body{display:flex;gap:16px;padding:4px 14px}
.testi-body p{font-size:11px;color:var(--muted);line-height:1.6}
.testi-person{width:100px;flex:none}
.avatar{width:76px;height:76px;border-radius:50%;background:linear-gradient(135deg,#c8b4a0,#8d7766)}
.testi-name{font-size:10px;font-weight:700;margin-top:6px;color:var(--ink);white-space:nowrap}

/* newsletter */
.newsletter{position:absolute;top:2208px;left:0;width:1200px;height:56px;background:var(--red);display:flex;align-items:center;justify-content:center;gap:20px;color:var(--white)}
.newsletter h3{font-size:18px;font-weight:400}
.newsletter .field{width:240px;height:26px;background:var(--white);color:#999;font-size:10px;padding:6px 8px}
.newsletter .btn{background:var(--footer);color:var(--white);font-size:11px;padding:6px 14px}

/* footer */
.site-footer{position:absolute;top:2264px;left:0;width:1200px;height:196px;background:var(--footer);color:#ccc}
.fcol{position:absolute;top:22px}
.fcol h4{color:var(--white);font-size:13px;font-weight:600;margin-bottom:12px}
.fcol li{list-style:none;font-size:10px;line-height:1.95}
.contact-row{display:flex;gap:8px;font-size:10px;line-height:1.5;margin-bottom:6px}
.contact-row i{width:14px;height:14px;border-radius:50%;background:var(--red);flex:none;display:block}
.badges{display:flex;gap:12px;flex-wrap:wrap;width:200px}
.badges span{display:block;width:56px;height:44px;background:#ddd}
.follow li{display:flex;align-items:center;gap:8px;margin-bottom:4px}
.follow i{width:18px;height:18px;border-radius:50%;display:block;background:var(--red)}
.copyright{position:absolute;top:2460px;left:0;width:1200px;height:32px;background:var(--footer-deep);color:#999;font-size:10px;text-align:center;line-height:32px}
</style>
</head>
<body>

<header class="site-header">
  <div class="brand"><span class="brand-dot"></span><span class="brand-name">Tolvey Auction</span></div>
  <div class="topbar">
    <span><svg width="12" height="12" viewBox="0 0 24 24"><path fill="#c9202b" d="M6.6 10.8a15 15 0 0 0 6.6 6.6l2.2-2.2c.3-.3.7-.4 1-.2 1.1.4 2.3.6 3.6.6.6 0 1 .4 1 1V20c0 .6-.4 1-1 1A17 17 0 0 1 3 4c0-.6.4-1 1-1h3.5c.6 0 1 .4 1 1 0 1.3.2 2.5.6 3.6.1.3 0 .7-.2 1z"/></svg>(701) 555-0187</span>
    <span><svg width="13" height="10" viewBox="0 0 26 20"><rect x="1" y="1" width="24" height="18" fill="none" stroke="#c9202b" stroke-width="2"/><path d="M1 1l12 10L25 1" fill="none" stroke="#c9202b" stroke-width="2"/></svg>tolvey@tolveycompanies.example</span>
    <div class="social-dots"><i></i><i></i><i></i><i></i></div>
  </div>
  <nav class="main-nav">
    <a class="active">Home</a><a>Tolvey Services</a><a>Featured Projects</a><a>Results</a><a>Buying/Selling</a><a>About Tolvey</a><a>Contact Us</a>
  </nav>
</header>

<section class="hero" role="img" aria-label="Photograph of industrial machinery and pipework">
  <div class="hero-arrow" style="left:20px"><svg width="12" height="18" viewBox="0 0 12 18"><path d="M10 2L3 9l7 7" stroke="#fff" stroke-width="3" fill="none"/></svg></div>
  <div class="hero-arrow" style="right:20px"><svg width="12" height="18" viewBox="0 0 12 18"><path d="M2 2l7 7-7 7" stroke="#fff" stroke-width="3" fill="none"/></svg></div>
  <h1 class="hero-title">Let Our Experience<br>Work for You!</h1>
  <div class="btn-hero">GET STARTED</div>
</section>

<section class="services">
  <div class="tool-badge"><svg width="20" height="20" viewBox="0 0 24 24"><path d="M4 20l9-9M14 4a5 5 0 0 0 6 6l-3-3z" stroke="#555" stroke-width="2.5" fill="none" stroke-linecap="round"/><path d="M20 20l-9-9" stroke="#555" stroke-width="2.5" stroke-linecap="round"/></svg></div>
  <h2 class="section-title">Our Business <em>Services</em></h2>
  <div class="title-rule" style="top:106px"></div>
  <div class="svc-arrow" style="left:80px">&#8249;</div>
  <div class="svc-arrow" style="right:80px">&#8250;</div>

  <div class="service" style="left:137px">
    <div class="service-icon"><svg width="40" height="40" viewBox="0 0 40 40"><rect x="6" y="22" width="6" height="12" fill="#fff"/><rect x="17" y="14" width="6" height="20" fill="#fff"/><rect x="28" y="6" width="6" height="28" fill="#fff"/></svg></div>
    <h3>Marketing<br>Consultation</h3>
    <p>Lorem ipsum dolor sit amet, consectetur adipiscing elit, sed do eiusmod tempor.</p>
    <span class="btn-small">Read More</span>
  </div>
  <div class="service" style="left:361px">
    <div class="service-icon"><svg width="40" height="40" viewBox="0 0 40 40"><circle cx="20" cy="20" r="15" stroke="#fff" stroke-width="3" fill="none"/><circle cx="20" cy="20" r="8" stroke="#fff" stroke-width="3" fill="none"/><circle cx="20" cy="20" r="3" fill="#fff"/></svg></div>
    <h3>Marketing Plan<br>Implementation</h3>
    <p>Lorem ipsum dolor sit amet, consectetur adipiscing elit, sed do eiusmod tempor.</p>
    <span class="btn-small">Read More</span>
  </div>
  <div class="service" style="left:585px">
    <div class="service-icon"><svg width="40" height="40" viewBox="0 0 40 40"><circle cx="20" cy="20" r="12" stroke="#fff" stroke-width="6" stroke-dasharray="5 4" fill="none"/><circle cx="20" cy="20" r="5" fill="#fff"/></svg></div>
    <h3>Coordination of<br>Related Marketing</h3>
    <p>Lorem ipsum dolor sit amet, consectetur adipiscing elit, sed do eiusmod tempor.</p>
    <span class="btn-small">Read More</span>
  </div>
  <div class="service" style="left:809px">
    <div class="service-icon"><svg width="40" height="40" viewBox="0 0 40 40"><path d="M4 22l10-8 6 4 6-4 10 8-12 8z" fill="#fff"/></svg></div>
    <h3>Negotiated<br>Sales</h3>
    <p>Lorem ipsum dolor sit amet, consectetur adipiscing elit, sed do eiusmod tempor.</p>
    <span class="btn-small">Read More</span>
  </div>
</section>

<section class="welcome">
  <h2 class="section-title">Welcome To <em>Tolvey Companies</em></h2>
  <p>Lorem ipsum dolor sit amet, consectetur adipiscing elit, sed do eiusmod tempor incididunt ut labore et dolore magna aliqua. Ut enim ad minim veniam, quis nostrud exercitation ullamco laboris nisi ut aliquip ex ea commodo consequat. Duis aute irure dolor in reprehenderit in voluptate velit esse cillum dolore eu fugiat nulla pariatur excepteur sint occaecat.</p>
  <span class="btn-small">Read More</span>
</section>

<div class="panel" style="left:200px;top:1344px;width:500px;height:290px">
  <div class="panel-head"><span>Featured Projects</span><span>&#8249; &#8250;</span></div>
  <div class="thumbs">
    <div class="thumb"><div class="img" role="img" aria-label="Photograph of a house for sale"></div><h4>LOREM IPSUM DOLOR SIT</h4><p>Dolor sit amet consectetur adipiscing elit sed do.</p><span class="btn-small">View</span></div>
    <div class="thumb"><div class="img" role="img" aria-label="Photograph of a house for sale"></div><h4>LOREM IPSUM DOLOR SIT</h4><p>Dolor sit amet consectetur adipiscing elit sed do.</p><span class="btn-small">View</span></div>
    <div class="thumb"><div class="img" role="img" aria-label="Photograph of a house for sale"></div><h4>LOREM IPSUM DOLOR SIT</h4><p>Dolor sit amet consectetur adipiscing elit sed do.</p><span class="btn-small">View</span></div>
  </div>
</div>

<div class="panel" style="left:200px;top:1648px;width:500px;height:290px">
  <div class="panel-head"><span>Upcoming Events</span><span>&#8249; &#8250;</span></div>
  <div class="thumbs">
    <div class="thumb"><div class="img" role="img" aria-label="Photograph of an auction property"></div><h4>LOREM IPSUM DOLOR SIT</h4><p>Dolor sit amet consectetur adipiscing elit sed do.</p><span class="btn-small">View</span></div>
    <div class="thumb"><div class="img" role="img" aria-label="Photograph of an auction property"></div><h4>LOREM IPSUM DOLOR SIT</h4><p>Dolor sit amet consectetur adipiscing elit sed do.</p><span class="btn-small">View</span></div>
    <div class="thumb"><div class="img" role="img" aria-label="Photograph of an auction property"></div><h4>LOREM IPSUM DOLOR SIT</h4><p>Dolor sit amet consectetur adipiscing elit sed do.</p><span class="btn-small">View</span></div>
  </div>
</div>

<div class="panel" style="left:200px;top:1952px;width:500px;height:240px;background:transparent">
  <div class="testi-head"><svg width="22" height="18" viewBox="0 0 22 18"><path d="M2 2h18v10H9l-5 4v-4H2z" fill="#c9202b"/></svg>Client Testimonials</div>
  <div class="testi-body">
    <div class="testi-person"><div class="avatar" role="img" aria-label="Portrait of client"></div><div class="testi-name">Mrs. Jane Harlow</div></div>
    <p>Lorem ipsum dolor sit amet, consectetur adipiscing elit, sed do eiusmod tempor incididunt ut labore et dolore magna aliqua. Ut enim ad minim veniam, quis nostrud exercitation ullamco laboris nisi ut aliquip ex ea commodo consequat duis aute irure.</p>
  </div>
</div>

<div class="panel" style="left:720px;top:1344px;width:280px;height:216px">
  <div class="panel-head"><span>View Video</span></div>
  <div class="video" role="img" aria-label="Video still of a property">
    <div class="play"><svg width="18" height="20" viewBox="0 0 18 20"><path d="M2 1l15 9-15 9z" fill="#fff"/></svg></div>
  </div>
</div>

<div class="panel motd" style="left:720px;top:1568px;width:280px;height:104px">
  <h3>Message of the Day</h3>
  <p>Lorem ipsum dolor sit amet, consectetur adipiscing elit sed do eiusmod.</p>
</div>

<div class="panel" style="left:720px;top:1680px;width:280px;height:400px">
  <div class="panel-head"><span>News &amp; Events</span><span>View All</span></div>
  <div class="news-item"><div class="date"><b>01</b><small>JAN</small></div><div><h4>LOREM IPSUM DOLOR SIT AMET</h4><p>Consectetur adipiscing elit sed do eiusmod.</p></div></div>
  <div class="news-item"><div class="date"><b>08</b><small>JAN</small></div><div><h4>LOREM IPSUM DOLOR SIT AMET</h4><p>Consectetur adipiscing elit sed do eiusmod.</p></div></div>
  <div class="news-item"><div class="date"><b>15</b><small>JAN</small></div><div><h4>LOREM IPSUM DOLOR SIT AMET</h4><p>Consectetur adipiscing elit sed do eiusmod.</p></div></div>
  <div class="news-item"><div class="date"><b>22</b><small>JAN</small></div><div><h4>LOREM IPSUM DOLOR SIT AMET</h4><p>Consectetur adipiscing elit sed do eiusmod.</p></div></div>
  <div class="news-item"><div class="date"><b>29</b><small>JAN</small></div><div><h4>LOREM IPSUM DOLOR SIT AMET</h4><p>Consectetur adipiscing elit sed do eiusmod.</p></div></div>
</div>

<section class="newsletter">
  <h3>Subscribe to Our Newsletter</h3>
  <div class="field">Enter your email address</div>
  <div class="btn">Subscribe</div>
</section>

<footer class="site-footer">
  <div class="fcol" style="left:120px">
    <h4>Quick Links</h4>
    <ul><li>Home</li><li>Tolvey Services</li><li>Featured Projects</li><li>Results</li><li>Buying/Selling</li><li>About Tolvey</li><li>Contact Us</li></ul>
  </div>
  <div class="fcol" style="left:360px">
    <h4>Contact Us</h4>
    <div class="contact-row"><i></i><div>Tolvey Companies, Inc<br>P.O. Box 4382<br>Larkmoor, ND 58204</div></div>
    <div class="contact-row"><i></i><div>(701) 555-0187</div></div>
    <div class="contact-row"><i></i><div>Fax (701) 555-0143</div></div>
    <div class="contact-row"><i></i><div>tolvey@tolveycompanies.example</div></div>
  </div>
  <div class="fcol" style="left:640px">
    <h4>Our Affiliates</h4>
    <div class="badges"><span></span><span></span><span></span></div>
  </div>
  <div class="fcol follow" style="left:920px">
    <h4>Follow Us</h4>
    <ul>
      <li><i></i>Chatterbook</li>
      <li><i></i>Chirper</li>
      <li><i></i>Linkwork</li>
      <li><i></i>Searchly+</li>
    </ul>
  </div>
</footer>
<div class="copyright">Copyright © 2015 Tolvey Companies . All Right Reserved</div>

</body>
</html>
```